Bref créative
Larchmere Restoring LLC
Bringing new life to old wood
Professional
Trent Holloway
owner
larchmererestore@mailvox.net
I need the following listed on the card.
Owners:
Trent Holloway 555 274 1906
Darby Fennimore 555 381 4527
Licensed and Insured
Free Estimates.
Hardwood floors and Cabinets. If it's made of wood we can renew it. Color changes or tints. Low odor, dust, and mess. A fraction of the cost vs refacing or replacement. Quick turnaround. Most jobs completed in 1-2 days.

```html
<!DOCTYPE html>
<html lang="en">
<head>
<meta charset="utf-8">
<title>Larchmere Restoring LLC – Envelope Set</title>
<link href="https://fonts.googleapis.com/css2?family=Cinzel:wght@600&family=Open+Sans:wght@400;600&display=swap" rel="stylesheet">
<style>
  :root {
    --stage: #000000;
    --paper: #ffffff;
    --wood-dark: #2a2a2a;
    --wood-mid: #3a3a3a;
    --wood-deep: #1b1b1b;
    --copper-light: #c07a55;
    --copper: #a45a38;
    --copper-dark: #7a3e24;
    --silver: #c9c6c2;
    --brand-ink-light: #e6e1dc;
    --brand-ink-dark: #7b6a5e;
    --window-grey: #e9e9e9;
    --contact-ink: #f3e6dc;
  }
  * { box-sizing: border-box; margin: 0; padding: 0; }
  html, body { width: 1200px; height: 626px; overflow: hidden; background: var(--stage); }
  .canvas { position: relative; width: 1200px; height: 626px; background: var(--stage); }

  .envelope { position: absolute; width: 540px; height: 221px; overflow: hidden; }
  .envelope--back  { left: 43px;  top: 48px;  background: var(--paper); }
  .envelope--front-light { left: 43px; top: 348px; background: var(--paper); }
  .envelope--front-dark-left  { left: 624px; top: 48px; }
  .envelope--front-dark-center { left: 624px; top: 348px; }

  .wood-surface {
    position: absolute; inset: 0;
    background: linear-gradient(100deg, var(--wood-deep) 0%, var(--wood-mid) 35%, var(--wood-dark) 60%, var(--wood-deep) 100%);
  }
  .copper-band {
    position: absolute; left: 0; right: 0; bottom: 0; height: 52px;
    background: linear-gradient(90deg, var(--copper-dark), var(--copper-light) 45%, var(--copper) 100%);
  }
  .copper-band--thin { height: 8px; }
  .silver-rule { position: absolute; left: 0; right: 0; bottom: 8px; height: 3px; background: var(--silver); }

  .flap { position: absolute; left: 0; top: 0; width: 540px; height: 80px; }

  .brand { position: absolute; display: flex; align-items: center; gap: 8px; }
  .brand-square { width: 30px; height: 30px; background: linear-gradient(135deg, #d8d2cc, #8c847c); }
  .brand-name {
    font-family: "Cinzel", serif; font-weight: 600; font-size: 15px; letter-spacing: 1px;
    line-height: 1.15; width: 150px;
  }
  .brand--light .brand-name { color: var(--brand-ink-light); }
  .brand--dark .brand-name { color: var(--brand-ink-dark); }

  .brand--flap { left: 250px; top: 14px; }
  .brand--flap .brand-square { width: 28px; height: 28px; }

  .brand--corner { left: 24px; top: 22px; }
  .brand--stacked { left: 50%; top: 24px; transform: translateX(-50%); flex-direction: column; gap: 6px; text-align: center; }
  .brand--stacked .brand-name { width: 220px; }

  .address-window { position: absolute; left: 26px; top: 140px; width: 252px; height: 48px; background: var(--window-grey); }

  .contacts {
    position: absolute; right: 60px; bottom: 12px; display: flex; gap: 26px;
    font-family: "Open Sans", sans-serif; color: var(--contact-ink); font-size: 7px; line-height: 1.5;
  }
  .contact-name { font-weight: 600; text-transform: uppercase; letter-spacing: .5px; }
  .band-square { position: absolute; left: 16px; bottom: 16px; width: 18px; height: 18px; border: 1px solid var(--contact-ink); opacity: .7; }
  .band-square--right { left: auto; right: 18px; }
</style>
</head>
<body>
<main class="canvas">

  <section class="envelope envelope--back" aria-label="Envelope back">
    <svg class="flap" viewBox="0 0 540 80" role="img" aria-label="Dark wood grain flap">
      <defs>
        <linearGradient id="flapWood" x1="0" x2="1" y1="0" y2="0">
          <stop offset="0" stop-color="#1b1b1b"/><stop offset=".5" stop-color="#3a3a3a"/><stop offset="1" stop-color="#1b1b1b"/>
        </linearGradient>
      </defs>
      <path d="M0 0 H540 V18 L300 74 Q270 80 240 74 L0 18 Z" fill="url(#flapWood)"/>
    </svg>
    <div class="brand brand--flap brand--light">
      <span class="brand-square"></span>
    </div>
  </section>

  <section class="envelope envelope--front-dark-left" aria-label="Envelope front, corner logo">
    <div class="wood-surface" role="img" aria-label="Dark wood grain texture"></div>
    <div class="brand brand--corner brand--light">
      <span class="brand-square"></span>
      <span class="brand-name">Larchmere Restoring LLC</span>
    </div>
    <div class="copper-band" role="img" aria-label="Warm copper wood band"></div>
    <span class="band-square"></span>
    <div class="contacts">
      <p><span class="contact-name">Trent Holloway</span><br>555 274 1906</p>
      <p><span class="contact-name">Darby Fennimore</span><br>555 381 4527</p>
      <p><span class="contact-name">Email</span><br>larchmererestore@mailvox.net</p>
    </div>
  </section>

  <section class="envelope envelope--front-light" aria-label="Envelope front, white with address window">
    <div class="brand brand--corner brand--dark">
      <span class="brand-square"></span>
      <span class="brand-name">Larchmere Restoring LLC</span>
    </div>
    <div class="address-window"></div>
    <div class="silver-rule"></div>
    <div class="copper-band copper-band--thin" role="img" aria-label="Thin copper wood band"></div>
  </section>

  <section class="envelope envelope--front-dark-center" aria-label="Envelope front, centered logo">
    <div class="wood-surface" role="img" aria-label="Dark wood grain texture"></div>
    <div class="brand brand--stacked brand--light">
      <span class="brand-square"></span>
      <span class="brand-name">Larchmere Restoring LLC</span>
    </div>
    <div class="copper-band" role="img" aria-label="Warm copper wood band"></div>
    <span class="band-square band-square--right"></span>
    <div class="contacts">
      <p><span class="contact-name">Trent Holloway</span><br>555 274 1906</p>
      <p><span class="contact-name">Darby Fennimore</span><br>555 381 4527</p>
      <p><span class="contact-name">Email</span><br>larchmererestore@mailvox.net</p>
    </div>
  </section>

</main>
</body>
</html>
```